Presentation Folder for dental clinic

We need a presentation folder design. The presentation folder is what we give to our patients with treatment plans, quotes, images, information sheets etc.
I have uploaded current stationary designs for assistance as well as a photo of our external sign design.
We are an upmarket dental clinic.
Professionalism and customer service is key to us.
We provide information in presentation folders to give to patients.
It needs to memorable and a statement to who we are.

Target Market(s)

Main patient base is Male and Female 40 years old to 70 years old

Industry/Entity Type

Dental Clinic

Font styles to use
Serif
Sans Serif

Requirements
Must have
• Design:
• -Professional
• -Timeless
• -Modern
• - Memorable
• - Statement (if a patient puts down the folder, it will be easily identifiable with as Corvel Dentals folder)
• Logo
• Address, phone, email, website
• Dr Leo Brandt name and degree details
• Colour scheme to match current logos and branding
• "Your Smile Our Passion" quote
Nice to have
• Services listed:
• - Sleep Dentistry
• - Happy Gas
• - Dental Implants
• - Cosmetic Dentistry
• - Oral Surgery
• - Alignora
• - Teeth Whitening
• - General Dentistry
• - Childrens Dentistry
• See website www.corveldental-example.com.au
Should not have
• Dental cliche photos

```html
<!DOCTYPE html>
<html lang="en">
<head>
<meta charset="utf-8">
<title>Corvel Dentals – Presentation Folder</title>
<link href="https://fonts.googleapis.com/css2?family=Open+Sans:wght@400;600;700&display=swap" rel="stylesheet">
<style>
  :root{
    --purple:#8a3f97;
    --purple-light:#a463b0;
    --purple-deep:#6f2f7c;
    --grey-text:#7b7b7b;
    --grey-dark:#5c5c5c;
    --band-grey:#ececec;
    --paper:#ffffff;
    --backdrop:#e7dbe7;
  }
  *{box-sizing:border-box;margin:0;padding:0}
  html,body{width:1200px;height:847px;overflow:hidden}
  body{background:var(--backdrop);font-family:"Open Sans",sans-serif;position:relative}

  .folder-panel{position:absolute;top:44px;width:540px;height:760px;background:var(--paper);overflow:hidden;box-shadow:0 6px 24px rgba(80,40,90,.18)}
  .back-cover{left:60px}
  .front-cover{left:600px}
  .panel-art{position:absolute;inset:0;width:540px;height:760px}

  /* back cover */
  .goal-line{position:absolute;top:40px;right:30px;text-align:right;color:var(--grey-text);font-size:23px;line-height:1.25}
  .goal-line strong{color:var(--purple);font-weight:600}
  .goal-line .goal-smile{color:var(--purple);font-weight:700}

  .contact-list{position:absolute;top:500px;left:38px;list-style:none;font-size:12.5px;font-weight:600;color:var(--grey-dark)}
  .contact-list li{display:flex;align-items:center;gap:10px;margin-bottom:5px}
  .contact-list .address{color:var(--purple)}
  .contact-icon{width:18px;height:18px;flex:none}

  .info-band{position:absolute;left:0;width:540px;background:var(--band-grey);color:var(--grey-text);font-size:11px;font-weight:600}
  .hours-band{top:608px;height:58px;padding:14px 30px 0}
  .services-band{top:690px;height:48px;padding:12px 20px 0;text-align:center}
  .band-tag{position:absolute;top:-11px;left:50%;transform:translateX(-50%);background:var(--purple);color:#fff;font-size:10.5px;font-weight:700;letter-spacing:.5px;padding:3px 22px;border-radius:0 0 12px 12px}
  .hours-table{display:grid;grid-template-columns:auto auto auto auto auto auto;column-gap:8px;row-gap:3px;justify-content:center}
  .hours-table .sep{color:var(--purple)}
  .services-list{line-height:1.6}
  .services-list .sep{color:var(--purple);padding:0 5px}

  /* front cover */
  .tagline{position:absolute;top:24px;left:22px;font-size:27px;line-height:1.3;color:var(--grey-text)}
  .tagline strong{color:var(--purple);font-weight:700}

  .doctor-credentials{position:absolute;top:470px;left:300px;color:var(--grey-text);font-size:8.5px;line-height:1.45}
  .doctor-name{display:flex;align-items:center;gap:8px;color:var(--purple);font-size:12px;font-weight:700;margin-left:-18px}
  .doctor-name svg{width:10px;height:10px}
  .doctor-credentials p{margin-left:0}

  .brand-block{position:absolute;top:560px;right:28px;text-align:right}
  .brand-name{color:var(--purple);font-size:44px;font-weight:600;letter-spacing:-.5px;line-height:1}
  .brand-sub{color:var(--grey-text);font-size:12.5px;font-weight:600;margin-top:6px}
</style>
</head>
<body>

<section class="folder-panel back-cover">
  <svg class="panel-art" viewBox="0 0 540 760" aria-hidden="false">
    <defs>
      <linearGradient id="photoBack" x1="0" y1="0" x2="1" y2="1">
        <stop offset="0" stop-color="#e9cdb8"/>
        <stop offset=".5" stop-color="#dcd6d8"/>
        <stop offset="1" stop-color="#b9cde0"/>
      </linearGradient>
    </defs>
    <rect x="0" y="0" width="540" height="12" fill="var(--purple)"/>
    <polygon points="0,52 540,150 540,460 0,420" fill="url(#photoBack)" role="img" aria-label="Photo of a smiling boy giving a thumbs up at the dental chair"/>
    <polygon points="0,44 540,142 540,152 0,54" fill="var(--purple)"/>
    <path d="M0,400 Q260,470 540,452 L540,482 Q260,505 0,448 Z" fill="var(--purple-light)"/>
    <path d="M0,440 Q260,498 540,476 L540,486 Q260,512 0,452 Z" fill="var(--purple-deep)"/>
    <rect x="0" y="742" width="540" height="18" fill="var(--purple)"/>
  </svg>

  <p class="goal-line"><strong>Our goal</strong> is help you<br>show off your<br><span class="goal-smile">SMILE.</span></p>

  <ul class="contact-list">
    <li class="address">
      <svg class="contact-icon" viewBox="0 0 18 18"><circle cx="9" cy="9" r="9" fill="var(--purple)"/><path d="M4.5 9.2 9 5l4.5 4.2h-1.4V13H10v-2.5H8V13H5.9V9.2z" fill="#fff"/></svg>
      41 Larkmoor St, Elmvale VIC 3999.
    </li>
    <li>
      <svg class="contact-icon" viewBox="0 0 18 18"><circle cx="9" cy="9" r="9" fill="var(--purple)"/><path d="M6 4.5h2l.8 2.3-1.2.9a6 6 0 0 0 2.7 2.7l.9-1.2 2.3.8v2a1 1 0 0 1-1 1A8 8 0 0 1 5 5.5a1 1 0 0 1 1-1z" fill="#fff"/></svg>
      03 9000 4127
    </li>
    <li>
      <svg class="contact-icon" viewBox="0 0 18 18"><circle cx="9" cy="9" r="9" fill="var(--purple)"/><rect x="4.5" y="6" width="9" height="6.5" rx="1" fill="#fff"/><path d="M4.8 6.3 9 9.5l4.2-3.2" stroke="var(--purple)" stroke-width="1" fill="none"/></svg>
      info@corveldental-example.com.au
    </li>
    <li>
      <svg class="contact-icon" viewBox="0 0 18 18"><circle cx="9" cy="9" r="9" fill="var(--purple)"/><circle cx="8" cy="8" r="3" stroke="#fff" stroke-width="1.5" fill="none"/><path d="m10.2 10.2 3 3" stroke="#fff" stroke-width="1.6"/></svg>
      www.corveldental-example.com.au
    </li>
  </ul>

  <div class="info-band hours-band">
    <span class="band-tag">OPENING HOURS</span>
    <div class="hours-table">
      <span>Monday</span><span class="sep">|</span><span>9:00am – 5:00pm</span><span class="sep">|</span><span>Tuesday</span><span>9:00am – 7:00pm</span>
      <span>Wednesday*</span><span class="sep">|</span><span>9:00am – 1:00pm</span><span class="sep">|</span><span>Thursday</span><span>9:00am – 5:00pm</span>
      <span></span><span></span><span></span><span class="sep">|</span><span>Friday</span><span>7:30am – 2:00pm</span>
    </div>
  </div>

  <div class="info-band services-band">
    <span class="band-tag">SERVICES</span>
    <p class="services-list">
      Sleep Dentistry<span class="sep">|</span>Happy Gas<span class="sep">|</span>Dental Implants<span class="sep">|</span>Cosmetic Dentistry<span class="sep">|</span>Oral Surgery<br>
      Alignora<span class="sep">|</span>Teeth Whitening<span class="sep">|</span>General Dentistry<span class="sep">|</span>Childrens Dentistry
    </p>
  </div>
</section>

<section class="folder-panel front-cover">
  <svg class="panel-art" viewBox="0 0 540 760">
    <defs>
      <linearGradient id="photoFront" x1="0" y1="0" x2="1" y2="1">
        <stop offset="0" stop-color="#d8dde3"/>
        <stop offset=".45" stop-color="#ecd2c2"/>
        <stop offset="1" stop-color="#9fd3dc"/>
      </linearGradient>
    </defs>
    <rect x="0" y="0" width="540" height="12" fill="var(--purple)"/>
    <polygon points="300,12 540,12 540,240 0,480 0,190" fill="url(#photoFront)" role="img" aria-label="Photo of a smiling girl in the dental chair beside a dental mirror"/>
    <polygon points="290,12 304,12 0,196 0,184" fill="var(--purple)"/>
    <polygon points="540,228 540,300 0,540 0,468" fill="var(--purple-light)"/>
    <polygon points="0,560 0,742 290,742" fill="var(--purple)"/>
    <rect x="0" y="742" width="540" height="18" fill="var(--purple)"/>
  </svg>

  <p class="tagline">Your <strong>SMILE</strong><br>Our Passion</p>

  <div class="doctor-credentials">
    <p class="doctor-name"><svg viewBox="0 0 10 10"><polygon points="0,0 10,5 0,10" fill="var(--purple)"/></svg>Dr Leo Brandt</p>
    <p>B.D.S. Ashford College</p>
    <p>Graduate Diploma in Clinical Dentistry</p>
    <p>(IV Sedation &amp; Pain Control) Northbay University</p>
  </div>

  <div class="brand-block">
    <p class="brand-name">Corvel Dentals</p>
    <p class="brand-sub">Centre for Aesthetic, Implant &amp; Sedation Dentistry</p>
  </div>
</section>

</body>
</html>
```